Law firm Seeks Modern and Engaging Site Redesign

Law firm seeks a new web site. Should be modern, but retaining existing logo. Needs to include contact section, professional bio, services offered, and contact information.

The site should be modern, responsive, and able to be SEO optimized.

The finished product should be coded in a Wordpress site, which I will provide. I can work with other platforms, including Wix, but WP is preferred.

Note the current site is https://www.tallowfieldlaw.example/#/home

Target Market(s)

Family Law Practice

Industry/Entity Type

Legal

Coding

Coded - Design and coding required

Number of Pages Required

4 page

Font styles to use
Sans Serif

Requirements
Must have
• Service description
Bio pages for partners
Contact Form
Awards/Publication page

```html
<!DOCTYPE html>
<html lang="en">
<head>
<meta charset="utf-8">
<title>Tallowfield Marsh — Attorneys at Law</title>
<link rel="stylesheet" href="https://fonts.googleapis.com/css2?family=Marcellus&family=Poppins:wght@300;400;500;600&display=swap">
<style>
:root{
  --blue:#3f51a0;
  --blue-bright:#4c78e0;
  --navy:#1f3468;
  --gold:#a8913a;
  --grey-bar:#6b6b6b;
  --soft:#f4f4f4;
  --text:#6f6f6f;
  --dark:#2b2b2b;
  --white:#fff;
  --stage:#e9ebf0;
}
*{box-sizing:border-box;margin:0;padding:0}
html,body{width:1200px;height:2659px;overflow:hidden}
body{background:var(--stage);font-family:"Poppins",sans-serif;color:var(--text)}
.page{position:absolute;left:279px;top:140px;width:642px;height:2380px;background:var(--white);overflow:hidden;box-shadow:0 0 30px rgba(0,0,0,.12)}
section,header,footer,nav{position:absolute;left:0;width:642px}
.abs{position:absolute}
.serif{font-family:"Marcellus",serif}
.center{text-align:center;left:0;width:642px}

/* top bar */
.topbar{top:0;height:23px;background:var(--grey-bar)}
.social{top:8px;width:7px;height:7px;border-radius:50%;background:var(--white)}
.toplinks{right:180px;top:6px;font-size:5px;color:var(--white);font-weight:500;letter-spacing:.1px}
.toplinks span{margin:0 4px}
.quote-btn{left:479px;top:0;width:88px;height:23px;background:var(--blue);color:var(--white);font-size:6px;font-weight:600;text-align:center;line-height:23px}

/* header */
.masthead{top:23px;height:56px;background:var(--white)}
.divider{top:10px;width:1px;height:36px;background:#ddd}
.contact-label{font-size:5.5px;color:var(--text)}
.contact-value{font-size:8.5px;color:var(--blue);font-weight:500}
.brand{top:18px;left:0;width:642px;text-align:center;font-size:13px;color:var(--blue)}
.brand-mark{display:inline-block;width:8px;height:8px;background:var(--blue);margin-right:6px;vertical-align:1px}

/* nav */
.mainnav{top:79px;height:39px;background:var(--soft)}
.mainnav ul{list-style:none;display:flex;justify-content:center;padding-top:14px;font-size:8.5px;color:#777}
.mainnav li{position:relative}
.mainnav li+li:before{content:"|";margin:0 12px;color:#888}
.mainnav .active{color:var(--blue);font-weight:500}
.mainnav .active:after{content:"";position:absolute;left:0;right:0;top:-15px;height:2px;background:var(--blue)}

/* hero */
.hero{top:118px;height:239px;background:linear-gradient(100deg,#2b2a27 0%,#4a4843 40%,#3a3833 65%,#5a5346 100%)}
.hero-kicker{top:53px;font-size:9.5px;color:#eee}
.hero-title{top:67px;font-size:36px;color:var(--white);letter-spacing:.5px;font-weight:400}
.hero-text{top:113px;left:196px;width:250px;text-align:center;font-size:6.5px;color:#eee;line-height:1.4}
.btn-gold{background:var(--gold);color:var(--white);font-weight:500;text-align:center}
.hero .btn-gold{left:250px;top:157px;width:143px;height:27px;line-height:27px;font-size:7.5px;letter-spacing:.3px}

/* who we are */
.who{top:357px;height:386px;background:var(--white)}
h2.title{font-family:"Marcellus",serif;font-weight:400;color:var(--blue);font-size:20px;letter-spacing:.3px}
.who h2{left:78px;top:93px}
.para{font-size:5.7px;line-height:1.62;color:var(--text)}
.who .p1{left:78px;top:122px;width:222px}
.who .p2{left:78px;top:197px;width:222px}
.btn-blue{background:var(--blue);color:var(--white);font-size:6.5px;font-weight:500;text-align:center}
.who .btn-blue{left:78px;top:244px;width:61px;height:22px;line-height:22px}
.accent-block{left:444px;top:39px;width:140px;height:140px;background:var(--blue)}
.portrait{left:327px;top:55px;width:240px;height:261px;background:linear-gradient(160deg,#d9dee4 0%,#c6ccd4 40%,#39404e 60%,#2a303c 100%)}

/* services */
.services{top:743px;height:349px;background:var(--soft)}
.kicker{font-size:7.5px;color:#777}
.services .kicker{top:37px}
.services h2{top:50px}
.card{top:89px;width:156px;height:208px;background:var(--white)}
.card-img{left:0;top:0;width:156px;height:106px;background:linear-gradient(135deg,#6b3a22,#a4643b 50%,#3c2c25)}
.card-title{left:13px;width:135px;font-family:"Marcellus",serif;font-size:8.5px;color:var(--blue);line-height:1.15;font-weight:400}
.card-bar{left:0;width:2px;background:var(--blue)}
.card-text{left:13px;top:146px;width:130px;font-size:5.5px;line-height:1.5;color:#888}
.card-more{left:13px;top:186px;font-size:5.5px;color:#333;font-weight:500}

/* stats */
.stats{top:1092px;height:81px;background:linear-gradient(90deg,#4657a5,#5364b0 50%,#4a5ba8)}
.stat{top:26px;height:30px}
.stat svg{position:absolute;left:0;top:2px}
.stat .num{position:absolute;left:32px;top:-3px;font-family:"Marcellus",serif;font-size:16px;color:var(--white)}
.stat .lbl{position:absolute;left:32px;top:17px;font-family:"Marcellus",serif;font-style:italic;font-size:6.5px;color:var(--white);white-space:nowrap}

/* testimonial */
.testimonial{top:1173px;height:265px;background:var(--white)}
.testimonial .kicker{top:54px;font-size:8px}
.testimonial h2{top:67px}
.quote{top:111px;left:142px;width:358px;text-align:center;font-size:7px;line-height:1.55;color:var(--text)}
.avatar{left:303px;top:148px;width:36px;height:36px;border-radius:50%;border:2px solid var(--blue);background:linear-gradient(#d4d9e0,#7c8596)}
.who-said{top:188px;font-size:7.5px;font-weight:600;color:var(--dark)}
.said-date{top:198px;font-size:5.5px;color:#444}

/* consulting */
.consult{top:1438px;height:257px;background:linear-gradient(100deg,#4353a0,#4d5eab 60%,#4454a1)}
.consult h2{left:78px;top:52px;color:var(--white)}
.consult .sub{left:78px;top:75px;font-size:8.5px;color:#eef}
.consult .para{left:78px;top:104px;width:225px;color:#eef;font-size:7px;line-height:1.7}
.field{height:26px;border:1px solid #c9cfe9;font-size:5.5px;color:#eef;padding:9px 10px}
.consult .btn-gold{left:327px;top:178px;width:78px;height:27px;line-height:27px;font-size:6.5px}

/* blog */
.blog{top:1695px;height:345px;background:var(--soft)}
.blog .kicker{top:52px;font-size:8px}
.blog h2{top:65px}
.post{top:101px;width:156px;height:192px;background:var(--white)}
.post .card-img{height:105px}
.meta{left:13px;top:162px;font-size:5px;color:#aaa;display:flex;align-items:center;gap:6px}
.meta i{display:block;width:20px;height:20px;border-radius:50%;background:#ddd}

/* newsletter */
.newsletter{top:2040px;height:147px;background:var(--blue-bright)}
.newsletter h2{top:30px;color:var(--white);font-size:21px}
.newsletter .para{top:63px;left:170px;width:302px;text-align:center;color:#eef;font-size:5.5px;line-height:1.5}
.email{left:190px;top:85px;width:182px;height:28px;background:var(--navy);color:#ccd;font-size:5px;padding:11px 12px}
.subscribe{left:372px;top:85px;width:78px;height:28px;background:var(--white);color:var(--blue);font-size:8px;font-weight:600;text-align:center;line-height:28px}

/* footer */
.footer{top:2187px;height:193px;background:var(--navy);color:#dde}
.foot-brand{left:78px;top:56px;font-size:10px;color:var(--white)}
.foot-about{left:78px;top:79px;width:100px;font-size:5px;line-height:1.6;color:#dde}
.foot-col h3{font-family:"Marcellus",serif;font-weight:400;font-size:10px;color:var(--white);letter-spacing:.3px}
.foot-col ul{list-style:none;margin-top:11px;font-size:6px;line-height:15.5px}
.foot-col p{font-size:6px;line-height:1.3;margin-top:11px}
.copyright{top:176px;font-size:5.5px;color:#dde}
</style>
</head>
<body>
<div class="page">

  <div class="topbar abs" style="left:0;width:642px">
    <span class="social abs" style="left:78px"></span>
    <span class="social abs" style="left:97px"></span>
    <span class="social abs" style="left:116px"></span>
    <div class="toplinks abs">Make A Claim<span>|</span>Services<span>|</span>Solution Center</div>
    <div class="quote-btn abs">Get A Quotes</div>
  </div>

  <header class="masthead">
    <svg class="abs" style="left:78px;top:19px" width="16" height="16" viewBox="0 0 24 24"><path fill="#3f51a0" d="M6.6 10.8a15.1 15.1 0 0 0 6.6 6.6l2.2-2.2c.3-.3.7-.4 1-.2 1.1.4 2.3.6 3.6.6.6 0 1 .4 1 1V20c0 .6-.4 1-1 1C10.6 21 3 13.4 3 4c0-.6.4-1 1-1h3.5c.6 0 1 .4 1 1 0 1.3.2 2.5.6 3.6.1.3 0 .7-.2 1l-2.3 2.2z"/></svg>
    <div class="abs" style="left:104px;top:18px"><div class="contact-label">Call Us On</div><div class="contact-value">+555-010-2741</div></div>
    <span class="divider abs" style="left:214px"></span>
    <div class="brand abs serif"><span class="brand-mark"></span>Tallowfield Marsh</div>
    <span class="divider abs" style="left:428px"></span>
    <div class="abs" style="right:100px;top:16px;text-align:right"><div class="contact-label">Request on</div><div class="contact-value">Get Appoinments</div></div>
    <svg class="abs" style="left:550px;top:19px" width="17" height="17" viewBox="0 0 20 20"><circle cx="10" cy="10" r="9" fill="#3f51a0"/><path d="M10 4.5V10l3.5 2.5" stroke="#fff" stroke-width="1.8" fill="none" stroke-linecap="round"/></svg>
  </header>

  <nav class="mainnav">
    <ul><li class="active">Home</li><li>Family Law</li><li>Criminal Law</li><li>About</li><li>Contact</li></ul>
  </nav>

  <section class="hero" role="img" aria-label="Dark courtroom photograph with a judge's gavel and scales of justice">
    <div class="hero-kicker abs center">A Better Legal System</div>
    <h1 class="hero-title abs center serif">Great Law Firm</h1>
    <p class="hero-text abs">Lorem Ipsum is simply dummy text of the printing and typesetting industry. Lorem Ipsum has been the industry's standard.</p>
    <div class="btn-gold abs">FREE CASE EVALUATION</div>
  </section>

  <section class="who">
    <h2 class="title abs">WHO WE ARE</h2>
    <p class="para abs p1">The law firm of Tallowfield Marsh, LLC is based in Alder County, conveniently located in Brookhollow, New Jersey in 18 Alder Court. We serve the needs of clients throughout Alder County, as well as, clients from several other counties, including, but not limited to, Linden, Fairmont, Ashby and Riverton. Between our partners, we have over 30+ years of experience assisting clients with all of their family law and criminal law needs.</p>
    <p class="para abs p2">Often times the areas of family law and criminal law cross paths, which can be both emotionally and financially complex. We understand that our client's case is unique and pride ourselves on being responsive to all of our clients needs.</p>
    <div class="btn-blue abs">Read More</div>
    <div class="accent-block abs"></div>
    <div class="portrait abs" role="img" aria-label="Portrait photo of a partner in a dark suit in a bright office"></div>
  </section>

  <section class="services">
    <div class="kicker abs center">HOW CAN WE HELP YOU</div>
    <h2 class="title abs center">OUR SERVICES</h2>
    <article class="card abs" style="left:78px">
      <div class="card-img abs" role="img" aria-label="Lawyer speaking with clients at a courtroom table"></div>
      <span class="card-bar abs" style="top:124px;height:16px"></span>
      <h3 class="card-title abs" style="top:126px">Family Lawyer</h3>
      <p class="card-text abs">Lorem ipsum is simply dummy text of the printing and typesetting industry. Lorem ipsum has been the industry's standard dummy text ever since the 1500s,</p>
      <div class="card-more abs">Read More ›</div>
    </article>
    <article class="card abs" style="left:244px">
      <div class="card-img abs" role="img" aria-label="Full courtroom with jury and attorneys"></div>
      <span class="card-bar abs" style="top:126px;height:16px"></span>
      <h3 class="card-title abs" style="top:128px">Criminal Lawyer</h3>
      <p class="card-text abs">Lorem ipsum is simply dummy text of the printing and typesetting industry. Lorem ipsum has been the industry's standard dummy text ever since the 1500s,</p>
      <div class="card-more abs">Read More ›</div>
    </article>
    <article class="card abs" style="left:410px">
      <div class="card-img abs" role="img" aria-label="Attorney handing documents to a judge at the bench"></div>
      <span class="card-bar abs" style="top:124px;height:16px"></span>
      <h3 class="card-title abs" style="top:126px">Financial Lawyer</h3>
      <p class="card-text abs">Lorem ipsum is simply dummy text of the printing and typesetting industry. Lorem ipsum has been the industry's standard dummy text ever since the 1500s,</p>
      <div class="card-more abs">Read More ›</div>
    </article>
  </section>

  <section class="stats">
    <div class="stat abs" style="left:78px">
      <svg width="24" height="24" viewBox="0 0 24 24"><circle cx="12" cy="12" r="11" fill="none" stroke="#fff" stroke-width="1.3"/><path d="M8 15l5-5M11 8l4 4M7 17h6" stroke="#fff" stroke-width="1.6" stroke-linecap="round"/></svg>
      <div class="num">50</div><div class="lbl">Years of Exercience</div>
    </div>
    <div class="stat abs" style="left:203px">
      <svg width="24" height="24" viewBox="0 0 24 24"><circle cx="12" cy="12" r="11" fill="none" stroke="#fff" stroke-width="1.3"/><circle cx="12" cy="10" r="3" fill="#fff"/><path d="M7 17c1-3 9-3 10 0z" fill="#fff"/></svg>
      <div class="num">984</div><div class="lbl">Satisfied Clients</div>
    </div>
    <div class="stat abs" style="left:327px">
      <svg width="24" height="24" viewBox="0 0 24 24"><circle cx="12" cy="12" r="11" fill="none" stroke="#fff" stroke-width="1.3"/><path d="M7 10l2-3h6l2 3-5 7z" fill="none" stroke="#fff" stroke-width="1.3" stroke-linejoin="round"/></svg>
      <div class="num">2,450</div><div class="lbl">Cases Won</div>
    </div>
    <div class="stat abs" style="left:451px">
      <svg width="24" height="24" viewBox="0 0 24 24"><circle cx="12" cy="12" r="11" fill="none" stroke="#fff" stroke-width="1.3"/><circle cx="9" cy="10" r="2" fill="#fff"/><circle cx="15" cy="10" r="2" fill="#fff"/><path d="M6 16c.5-2.5 5.5-2.5 6 0zM12 16c.5-2.5 5.5-2.5 6 0z" fill="#fff"/></svg>
      <div class="num">4,505</div><div class="lbl">Number of Lawyers</div>
    </div>
  </section>

  <section class="testimonial">
    <div class="kicker abs center">What People Say</div>
    <h2 class="title abs center">CLIENT TESTIMONIAL</h2>
    <svg class="abs" style="left:92px;top:128px" width="10" height="16" viewBox="0 0 10 16"><path d="M8 1L2 8l6 7" stroke="#666" stroke-width="1.3" fill="none"/></svg>
    <p class="quote abs">Lorem Ipsum is simply dummy text of the printing and typesetting industry. Lorem Ipsum has been the industry's standard dummy text ever since the 1500s, when an unknown printer took a galley of type and scrambled it to make a type specimen book.</p>
    <svg class="abs" style="left:541px;top:128px" width="10" height="16" viewBox="0 0 10 16"><path d="M2 1l6 7-6 7" stroke="#666" stroke-width="1.3" fill="none"/></svg>
    <div class="avatar abs" role="img" aria-label="Client portrait photo"></div>
    <div class="who-said abs center">John Doe</div>
    <div class="said-date abs center">24 Feb, 2020</div>
  </section>

  <section class="consult" role="img" aria-label="Blue-tinted photo of a gavel and law books">
    <h2 class="title abs">FREE CONSULTING</h2>
    <div class="sub abs">Call us 24/7 at (555)010-4567 or fill out the form.</div>
    <p class="para abs">It is a long established fact that a reader will be distracted by the readable content of a page when looking at its layout. The point of using Lorem Ipsum is that it has a more-or-less able English content of a page.</p>
    <div class="field abs" style="left:327px;top:51px;width:115px">Name</div>
    <div class="field abs" style="left:452px;top:51px;width:115px">Phone</div>
    <div class="field abs" style="left:327px;top:84px;width:115px">Email</div>
    <div class="field abs" style="left:452px;top:84px;width:115px">Business Law</div>
    <div class="field abs" style="left:327px;top:117px;width:240px;height:53px;background:linear-gradient(90deg,transparent 30%,rgba(40,50,100,.45) 30%)">Case Description</div>
    <div class="btn-gold abs">APPOINTMENT</div>
  </section>

  <section class="blog">
    <div class="kicker abs center">Latest News</div>
    <h2 class="title abs center">FROM OUR BLOG</h2>
    <article class="post abs" style="left:78px">
      <div class="card-img abs" role="img" aria-label="Lawyer speaking with clients at a courtroom table"></div>
      <span class="card-bar abs" style="top:128px;height:20px"></span>
      <h3 class="card-title abs" style="top:128px">Who Can a Victim Sue after a Car Accident?</h3>
      <div class="meta abs"><i></i>By: Barristar &nbsp;|&nbsp; Nov 11 2019</div>
    </article>
    <article class="post abs" style="left:244px">
      <div class="card-img abs" role="img" aria-label="Full courtroom with jury and attorneys"></div>
      <span class="card-bar abs" style="top:130px;height:20px"></span>
      <h3 class="card-title abs" style="top:130px">Car Accidents Caused by Defective Vehicles</h3>
      <div class="meta abs"><i></i>By: Barristar &nbsp;|&nbsp; Nov 11 2019</div>
    </article>
    <article class="post abs" style="left:410px">
      <div class="card-img abs" role="img" aria-label="Attorney handing documents to a judge at the bench"></div>
      <span class="card-bar abs" style="top:128px;height:20px"></span>
      <h3 class="card-title abs" style="top:128px">Justice May For You If You Are Innocent</h3>
      <div class="meta abs"><i></i>By: Barristar &nbsp;|&nbsp; Nov 11 2019</div>
    </article>
  </section>

  <section class="newsletter">
    <h2 class="title abs center">Join Our Newsletter</h2>
    <p class="para abs">Lorem Ipsum is simply dummy text of the printing and typesetting industry. Lorem Ipsum has been the industry's standard dummy text ever since the 1500s.</p>
    <div class="email abs">Enter your Email</div>
    <div class="subscribe abs">SUBSCRIBE</div>
  </section>

  <footer class="footer">
    <div class="foot-brand abs serif">Tallowfield Marsh</div>
    <p class="foot-about abs">Contrary to popular belief, Lorem Ipsum is not simply random text. It has roots in a piece of classical Latin literature</p>
    <div class="foot-col abs" style="left:203px;top:50px"><h3>QUICK LINK</h3><ul><li>Home</li><li>About</li><li>Cases</li><li>Blog</li><li>Contact</li></ul></div>
    <div class="foot-col abs" style="left:327px;top:50px"><h3>PRACTICE AREA</h3><ul><li>Business Law</li><li>Family Law</li><li>Real Estate Law</li><li>Education Law</li><li>Criminal Law</li></ul></div>
    <div class="foot-col abs" style="left:451px;top:50px"><h3>PRACTICE AREA</h3>
      <p>Tallowfield &amp; Marsh LLC<br>18 Alder Court Suite 40<br>Brookhollow, NJ 07999</p>
      <p style="margin-top:8px">(555) 010-2741</p>
      <p style="margin-top:8px">(555) 010-1257</p>
    </div>
    <div class="copyright abs center">© Copyright 2020 | Tallowfield &amp; Marsh LLC | All right reserved.</div>
  </footer>

</div>
</body>
</html>
```